Vorna Electric Construction We Light It Up!

We have an up coming meeting with a developer and general contractor. This card must bring out the best in my business. My business is an up and coming MDBE certified electrical contactor. I need a very powerful card to represent me business that we be bold and represent what I am about. WE LIGHT IT UP!

Target Market(s)

General Contractors, developers and property owners

Industry/Entity Type

Electrical

Contact Information for Business Card

great card that really brings out my bussiness

Colors
0355a3
3276b5
0393ce
34a6d7

Requirements
Must have
• Great design
Nice to have
• very different and noticeable card
Should not have
• open to anything

```html
<!DOCTYPE html>
<html lang="en">
<head>
<meta charset="utf-8">
<title>Vorna Electric Construction – Business Card</title>
<link rel="stylesheet" href="https://fonts.googleapis.com/css2?family=Open+Sans:ital,wght@0,400;0,600;1,400&display=swap">
<style>
  :root {
    --navy: #0355a3;
    --mid-blue: #3276b5;
    --bright-blue: #0393ce;
    --sky-blue: #34a6d7;
    --deep-blue: #0a3f7a;
    --paper: #ffffff;
    --ink-grey: #6b6f75;
    --stage: #e9ecef;
    --white: #ffffff;
  }
  * { box-sizing: border-box; margin: 0; padding: 0; }
  html, body { width: 1200px; height: 861px; overflow: hidden; }
  body {
    background: var(--stage);
    font-family: "Open Sans", Arial, sans-serif;
    display: flex;
    flex-direction: column;
    align-items: center;
    justify-content: center;
    gap: 30px;
  }
  .card {
    width: 680px;
    height: 389px;
    position: relative;
    overflow: hidden;
    box-shadow: 0 4px 14px rgba(0,0,0,0.12);
  }

  /* Front */
  .card-front {
    background: radial-gradient(ellipse at 55% 40%, var(--mid-blue) 0%, var(--navy) 55%, var(--deep-blue) 100%);
    display: flex;
    flex-direction: column;
    align-items: center;
    justify-content: center;
    gap: 18px;
  }
  .brand-mark {
    width: 26px;
    height: 26px;
    background: var(--white);
  }
  .front-name {
    color: var(--white);
    font-size: 30px;
    font-weight: 400;
    letter-spacing: 0.3px;
  }

  /* Back */
  .card-back { background: var(--paper); }
  .back-brand {
    position: absolute;
    left: 40px;
    top: 44px;
    display: flex;
    align-items: center;
    gap: 14px;
  }
  .back-brand .brand-mark { background: var(--navy); width: 30px; height: 30px; }
  .back-name {
    color: var(--bright-blue);
    font-size: 31px;
    font-weight: 400;
  }
  .person {
    position: absolute;
    left: 40px;
    top: 120px;
  }
  .person-name {
    color: var(--sky-blue);
    font-size: 21px;
    font-weight: 400;
    line-height: 1.1;
  }
  .person-role {
    color: var(--ink-grey);
    font-size: 14px;
    font-style: italic;
    margin-bottom: 12px;
  }
  .address {
    color: var(--ink-grey);
    font-size: 12.5px;
    line-height: 1.45;
    font-style: normal;
  }
  .contacts {
    position: absolute;
    right: 36px;
    top: 222px;
    list-style: none;
    color: var(--ink-grey);
    font-size: 13.5px;
  }
  .contacts li {
    display: flex;
    justify-content: flex-end;
    align-items: center;
    gap: 14px;
    height: 22px;
  }
  .contacts svg { width: 14px; height: 14px; fill: var(--sky-blue); }
  .contact-row { display: flex; gap: 24px; }
  .band-line {
    position: absolute;
    left: 0; right: 0;
    top: 316px;
    height: 4px;
    background: var(--sky-blue);
    opacity: 0.35;
  }
  .band {
    position: absolute;
    left: 0; right: 0; bottom: 0;
    height: 64px;
    background: var(--navy);
  }
</style>
</head>
<body>
  <section class="card card-front" aria-label="Card front">
    <div class="brand-mark"></div>
    <h1 class="front-name">Vorna Electric Construction</h1>
  </section>

  <section class="card card-back" aria-label="Card back">
    <div class="back-brand">
      <div class="brand-mark"></div>
      <h2 class="back-name">Vorna Electric Construction</h2>
    </div>

    <div class="person">
      <p class="person-name">YOUR NAME</p>
      <p class="person-role">Director</p>
      <address class="address">
        Your address - Kestrel Lane - Unit 4<br>
        P.o. Box 512 Marrow, Tel 4410<br>
        Dunmore 20817, NSW 61254B,<br>
        Reg B4830519
      </address>
    </div>

    <ul class="contacts">
      <li>
        <span class="contact-row"><span>yourname@vornaelectric.com.nn</span><span>045318276</span></span>
        <svg viewBox="0 0 14 14" aria-hidden="true"><rect x="3" y="0" width="8" height="14" rx="1.5"/><rect x="4.5" y="2" width="5" height="8" fill="#fff"/></svg>
      </li>
      <li>
        <span>www.vornaelectric.com.nn</span>
        <svg viewBox="0 0 14 14" aria-hidden="true"><rect x="0" y="3" width="14" height="9" rx="1"/><path d="M1 4 L7 8.5 L13 4" stroke="#fff" stroke-width="1.2" fill="none"/></svg>
      </li>
      <li>
        <svg viewBox="0 0 14 14" aria-hidden="true"><path d="M7 1 L13 7 L11 7 L11 13 L8.5 13 L8.5 9 L5.5 9 L5.5 13 L3 13 L3 7 L1 7 Z"/></svg>
      </li>
    </ul>

    <div class="band-line"></div>
    <div class="band"></div>
  </section>
</body>
</html>
```